International Hand & Body company needing a Hand cream tube design for the Retail market

I am wanting a modern design for a new range of 6 hand creams I will be launching in August. They need to compliment our range of wrapped soaps which you can see on www.plomvane.com.au so am wanting clean designs. I am wanting a solid colour with a hand drawn organic feel line drawing in black elegantly placed wrapping around the label. I am wanting to focus on the colour and positioning of words and fonts. I like modern clean contemporary fonts. The final design needs to appeal to the broader female market.This may lead to range expansion if designs are well received.
Updates

These designs are not hitting the brief. They are too generic and look like a supermarket brand. Our brand is more boutique and this design needs to be modern and simple. I would like more solid colours and more modern designs. Without patterns.

Target Market(s)

Female aged 20 - 70

Requirements
Must have
• a modern contemporary design that will appeal to the masses.
• Please read attached brief.
Should not have
• a black botanical illustration, in a loose and organic design to match the fragrance.

```html
<!DOCTYPE html>
<html lang="en">
<head>
<meta charset="utf-8">
<title>plomvane hand cream packaging</title>
<link rel="stylesheet" href="https://fonts.googleapis.com/css2?family=Open+Sans:wght@300;400;700&family=Antonio:wght@100..700&display=swap">
<style>
  :root {
    --bg: #efe0cf;
    --yellow: #fce683;
    --magenta: #b01e5a;
    --gold-dark: #c39a50;
    --gold-light: #f4e0b4;
    --ink: #1f1f1f;
    --grey: #8a8a86;
    --wood-light: #f3dcc0;
    --wood-dark: #deb78f;
  }
  * { margin: 0; padding: 0; box-sizing: border-box; }
  html, body { width: 1200px; height: 960px; overflow: hidden; background: var(--bg); }
  .board { position: relative; width: 1200px; height: 960px; background: var(--bg); font-family: "Open Sans", sans-serif; }
  .header-banner { position: absolute; left: 0; top: 0; width: 1200px; height: 180px; }
  .brand-title {
    position: absolute; left: 635px; top: 174px; transform: translateX(-50%);
    padding-left: 0.22em; white-space: nowrap;
    font-size: 88px; font-weight: 400; letter-spacing: 0.22em;
    color: var(--ink); line-height: 1;
  }

  .dieline { position: absolute; left: 122px; top: 314px; width: 400px; height: 590px; }
  .panel-yellow { position: absolute; left: 0; top: 0; width: 400px; height: 256px; background: var(--yellow); }
  .panel-gold { position: absolute; left: 0; top: 256px; width: 400px; height: 22px;
    background: linear-gradient(90deg, var(--gold-dark), var(--gold-light) 50%, var(--gold-dark)); }
  .panel-magenta { position: absolute; left: 0; top: 278px; width: 400px; height: 312px; background: var(--magenta); }
  .fold-line { position: absolute; left: 322px; top: 254px; width: 1px; height: 692px; background: #333; }

  .front-name { position: absolute; left: 29px; top: 221px; font-size: 26px; letter-spacing: 0.18em;
    color: #111; line-height: 1; white-space: nowrap; }
  .fragrance { position: absolute; left: 31px; top: 290px; font-family: "Antonio", sans-serif; font-weight: 200;
    font-size: 15px; letter-spacing: 0.08em; color: var(--yellow); line-height: 1; white-space: nowrap; }
  .front-foot { position: absolute; left: 32px; top: 510px; width: 82px; text-align: center; color: var(--yellow);
    font-family: "Antonio", sans-serif; font-weight: 200; line-height: 1.2; }
  .front-foot .type { font-size: 7px; letter-spacing: 0.12em; }
  .front-foot .origin { font-size: 9.5px; letter-spacing: 0.12em; margin-top: 6px; white-space: nowrap; }
  .front-foot .volume { font-family: "Open Sans", sans-serif; font-size: 5px; word-spacing: 6px; margin-top: 1px; }

  .side-name { position: absolute; right: 16px; top: 50px; font-size: 27px; letter-spacing: 0.18em;
    color: #111; line-height: 1; white-space: nowrap; }
  .tagline { position: absolute; right: 17px; top: 100px; text-align: right; white-space: nowrap;
    font-size: 15.5px; font-weight: 300; line-height: 21px; color: var(--grey); letter-spacing: -0.03em; }
  .ingredients { position: absolute; left: 279px; top: 290px; width: 109px; text-align: justify;
    font-size: 5.6px; line-height: 8.6px; font-weight: 700; color: var(--yellow); }
  .ingredients strong { font-weight: 700; }

  .mockup-area { position: absolute; left: 654px; top: 398px; width: 384px; height: 384px;
    background: linear-gradient(135deg, var(--wood-light), var(--wood-dark));
    box-shadow: 6px 14px 24px rgba(90, 60, 30, 0.25); }
</style>
</head>
<body>
<main class="board">
  <svg class="header-banner" viewBox="0 0 1200 180" aria-hidden="true">
    <defs>
      <linearGradient id="goldBand" x1="0" x2="1" y1="0" y2="0">
        <stop offset="0" stop-color="#c39a50"/>
        <stop offset="0.5" stop-color="#f4e0b4"/>
        <stop offset="1" stop-color="#c39a50"/>
      </linearGradient>
    </defs>
    <polygon points="0,0 610,0 610,146 0,52" fill="var(--yellow)"/>
    <polygon points="610,0 1200,0 1200,52 610,146" fill="var(--magenta)"/>
    <polygon points="0,52 610,146 1200,52 1200,62 610,170 0,62" fill="url(#goldBand)"/>
  </svg>

  <h1 class="brand-title">plomvane</h1>

  <section class="dieline">
    <div class="panel-yellow"></div>
    <div class="panel-gold"></div>
    <div class="panel-magenta"></div>

    <p class="front-name">plomvane</p>
    <p class="fragrance">CITRUS E EAGRASS</p>
    <div class="front-foot">
      <p class="type">HAND CREAM</p>
      <p class="origin">MADE IN AUSTRALIA</p>
      <p class="volume">35 mL 1.18 fl.oz</p>
    </div>

    <p class="side-name">plomvane</p>
    <p class="tagline">A nourishing<br>non-greasy hand<br>cream to keep skin<br>soft &amp; hydrated.</p>
    <p class="ingredients"><strong>INGREDIENTS:</strong> <span style="font-weight:400">AQUA, HELANTHUS ANNUUS SEED OIL, STEARIC ACID, GLYCERIN, CETEARYL ALCOHOL, CERA ALBA, GLYCERYL STEARATE, DIMETHICONE, PRUNUS AMYGDALUS DULCIS OIL ALMOND OIL, PAFUM, PHENOXYETHANOL, TRIETHANOLAMINE, TOCOPHERYL ACETATE, CAPRYLYL GLYCOL, SODIUM PCA, DISODIUM EDTA, ALOE BARBADENSIS LEAF JUICE POWDER (ALOE VERA), DECYLENE GLYCOL, THEOBROMA CACAO SEED BUTTER (COCOA), COCOS NUCIFERA (COCONUT) OIL, BUTYROSPERMUM PARKII (SHEA) BUTTER</span></p>
  </section>

  <div class="fold-line"></div>

  <div class="mockup-area" role="img" aria-label="Photograph of the boxed hand cream and tube lying on a light wooden board"></div>
</main>
</body>
</html>
```